Honey Jar Label Design

I am looking for a fun label design for a 1 lb honey jar.
The company is Corliss Waverly Botanicals, which sells cut flowers and is expanding into honey and eventually other honey products. I've included the design work for the business, and I'd like the honey products to coordinate with them but not necessarily match directly.
Label requirements:
Raw Honey
Corliss Waverly Botanicals
27308 Quarry Bend Rd
Bramford, NE 66341
NET WT. 16 OZ. (weight info must be in the lower third of the front label and easy to read)
Look and feel
Each slider illustrates characteristics of the customer's brand and the style your logo design should communicate.

```html
<!DOCTYPE html>
<html lang="en">
<head>
<meta charset="utf-8">
<title>Raw Honey Jar Labels – Corliss Waverly Botanicals</title>
<link rel="stylesheet" href="https://fonts.googleapis.com/css2?family=Caveat+Brush&family=Libre+Baskerville&family=Roboto:wght@400;700&display=swap">
<style>
  :root {
    --paper: #ffffff;
    --honey-yellow: #f8c315;
    --honey-orange: #f4962a;
    --ink: #0d0d0d;
    --caption-grey: #6d6e71;
    --outline: #444444;
  }
  * { box-sizing: border-box; margin: 0; padding: 0; }
  html, body { width: 1200px; height: 927px; overflow: hidden; background: var(--paper); }
  .canvas { position: relative; width: 1200px; height: 927px; font-family: "Roboto", Arial, sans-serif; color: var(--ink); }
  .abs { position: absolute; }
  .centered { transform: translate(-50%, -50%); text-align: center; }

  .lid, .label-body { position: absolute; }
  .lid { width: 150px; height: 150px; }
  .label-body { width: 267px; height: 431px; top: 292px; }

  .brand-seal {
    width: 104px; height: 104px; padding: 8px; border: 1.5px solid var(--ink); border-radius: 50%;
    display: flex; align-items: center; justify-content: center; text-align: center;
    font-family: "Libre Baskerville", Georgia, serif; font-size: 10px; line-height: 1.35; letter-spacing: 0.4px;
    text-transform: uppercase; color: var(--ink);
  }
  .brand-seal--small { width: 62px; height: 62px; padding: 4px; font-size: 6px; letter-spacing: 0.1px; line-height: 1.3; }
  .brand-seal--on-white { background: var(--paper); }

  .product-title { font-family: "Caveat Brush", cursive; color: var(--ink); white-space: nowrap; line-height: 1; font-weight: 400; }
  .product-title--one { font-size: 40px; }
  .product-title--two-raw { font-size: 92px; }
  .product-title--two-honey { font-size: 100px; }

  .maker-address { font-size: 10.5px; line-height: 1.25; white-space: nowrap; }
  .maker-address strong { font-weight: 700; }
  .net-weight { font-size: 10.5px; line-height: 1.05; white-space: nowrap; }
  .net-weight--bold { font-weight: 700; }

  .bee-illustration { background: var(--ink); border-radius: 46% 46% 50% 50%; }
  .bee-icon { background: linear-gradient(var(--ink), var(--honey-yellow)); border-radius: 50%; }

  .option-caption { font-size: 17px; color: var(--caption-grey); letter-spacing: 0.2px; }
</style>
</head>
<body>
<main class="canvas">

  <section class="design design--one">
    <svg class="lid" style="left:293px; top:128px" viewBox="0 0 150 150" role="img" aria-label="Yellow lid label ringed with small bee illustrations">
      <circle cx="75" cy="75" r="75" fill="var(--honey-yellow)"/>
      <circle cx="75" cy="75" r="64" fill="none" stroke="var(--ink)" stroke-width="10" stroke-opacity="0.85" stroke-dasharray="14 12"/>
    </svg>
    <div class="brand-seal brand-seal--small abs" style="left:368px; top:203px; transform:translate(-50%,-50%)">Corliss Waverly Botanicals</div>

    <svg class="label-body" style="left:235px" viewBox="0 0 267 431">
      <defs>
        <linearGradient id="honeyFill" x1="0" y1="0" x2="0" y2="1">
          <stop offset="0" stop-color="var(--honey-yellow)"/>
          <stop offset="0.55" stop-color="var(--honey-yellow)"/>
          <stop offset="1" stop-color="var(--honey-orange)"/>
        </linearGradient>
      </defs>
      <path role="img" aria-label="Yellow label with orange honeycomb pattern" fill="url(#honeyFill)"
        d="M92 0 L182 0 C205 10 260 80 265 200 C268 300 255 370 245 400 C240 420 230 431 215 431 L45 431 C30 431 20 420 18 400 C10 370 -2 300 1 200 C5 80 65 10 92 0 Z"/>
    </svg>

    <div class="brand-seal abs" style="left:368px; top:368px; transform:translate(-50%,-50%)">Corliss Waverly Botanicals</div>
    <h1 class="product-title product-title--one abs centered" style="left:368px; top:445px">Raw Honey</h1>
    <div class="bee-illustration abs" role="img" aria-label="Large black and yellow bee illustration" style="left:262px; top:470px; width:212px; height:140px"></div>
    <p class="net-weight abs centered" style="left:454px; top:630px">NET WT.<br>16 OZ</p>
    <p class="maker-address abs centered" style="left:368px; top:686px"><strong>Corliss Waverly Botanicals</strong><br>27308 Quarry Bend Rd.<br>Bramford, NE 66341</p>

    <p class="option-caption abs centered" style="left:368px; top:780px">Option ONE</p>
  </section>

  <section class="design design--two">
    <svg class="lid" style="left:696px; top:125px" viewBox="0 0 150 150">
      <defs><clipPath id="lidClip"><circle cx="75" cy="75" r="75"/></clipPath></defs>
      <circle cx="75" cy="75" r="75" fill="var(--honey-orange)"/>
      <g clip-path="url(#lidClip)" font-family="Caveat Brush, cursive" fill="var(--ink)">
        <text x="18" y="58" font-size="72">Raw</text>
        <text x="-12" y="112" font-size="72">Honey</text>
      </g>
      <circle cx="75" cy="75" r="36" fill="var(--paper)"/>
    </svg>
    <div class="brand-seal brand-seal--small brand-seal--on-white abs" style="left:771px; top:200px; transform:translate(-50%,-50%)">Corliss Waverly Botanicals</div>
    <div class="bee-icon abs" role="img" aria-label="Small bee icon" style="left:759px; top:245px; width:24px; height:18px"></div>

    <svg class="label-body" style="left:638px" viewBox="0 0 267 431">
      <defs>
        <linearGradient id="combFill" x1="0" y1="0" x2="0" y2="1">
          <stop offset="0" stop-color="var(--paper)"/>
          <stop offset="0.3" stop-color="var(--paper)"/>
          <stop offset="0.75" stop-color="var(--honey-orange)"/>
          <stop offset="1" stop-color="var(--honey-orange)"/>
        </linearGradient>
      </defs>
      <path role="img" aria-label="White label with orange honeycomb outlines" fill="url(#combFill)" stroke="var(--outline)" stroke-width="0.6"
        d="M92 0 L182 0 C205 10 260 80 265 200 C268 300 255 370 245 400 C240 420 230 431 215 431 L45 431 C30 431 20 420 18 400 C10 370 -2 300 1 200 C5 80 65 10 92 0 Z"/>
    </svg>

    <div class="brand-seal abs" style="left:771px; top:368px; transform:translate(-50%,-50%)">Corliss Waverly Botanicals</div>
    <h1 class="product-title product-title--two-raw abs centered" style="left:800px; top:482px">Raw</h1>
    <p class="product-title product-title--two-honey abs centered" style="left:772px; top:558px">Honey</p>
    <p class="maker-address abs centered" style="left:731px; top:650px"><strong>Corliss Waverly<br>Botanicals</strong><br>27308 Quarry Bend Rd.<br>Bramford, NE 66341</p>
    <div class="bee-icon abs" role="img" aria-label="Small bee icon" style="left:821px; top:654px; width:30px; height:20px"></div>
    <p class="net-weight net-weight--bold abs centered" style="left:835px; top:690px">NET WT.<br>16 OZ</p>

    <p class="option-caption abs centered" style="left:771px; top:780px">Option TWO</p>
  </section>

</main>
</body>
</html>
```